Quill Pet Shop Homepage

We are a pet shop, we focus on dog food / cat food / rodents & bird food

Based on WooCommerce

It should be a simple but professional homepage with an informative start page. In the shop it should then be possible to shop for products/manufacturers etc. Navigation/Filter menu on the left would be ideal.

Next menus:
ABOUT US
CONTACT
DOG
CAT
HOLDER

My Account - Login
My Cart

Footer:
Conditions
payment options
social media

In addition to our logo, I have attached 2 example pages from another shop which we would use as a guideline.

Target Market(s)

pet store

Industry/Entity Type

Animal, Pet Shop

Coding

Coded - Design and coding required

Number of Pages Required

1 page

Font styles to use
Sans Serif

Colors
0054AA
0677BA
7BADD7
CADEEF
E8F1F8

Requirements
Must have
• Main Page, Contact, About Us, Shop, Check Out, Member Login, Mailchimp Marketing - We work with WooCommerce

```html
<!DOCTYPE html>
<html lang="en">
<head>
<meta charset="utf-8">
<title>Quill Pet Shop – Premium Pet Food</title>
<link href="https://fonts.googleapis.com/css2?family=Raleway:wght@400;500;600;700;800&display=swap" rel="stylesheet">
<style>
:root{
  --blue-dark:#0054AA;
  --blue:#0677BA;
  --blue-mid:#7BADD7;
  --blue-light:#CADEEF;
  --blue-pale:#E8F1F8;
  --ink:#1a1a1a;
  --text:#555;
  --white:#fff;
}
*{box-sizing:border-box;margin:0;padding:0}
html,body{width:1200px;height:2634px;overflow:hidden}
body{position:relative;background:var(--white);font-family:"Raleway",sans-serif;color:var(--ink)}
.abs{position:absolute}
a{color:inherit;text-decoration:none}

/* header */
.site-header{position:absolute;left:0;top:0;width:1200px;height:74px;border-top:3px solid var(--blue-dark);border-bottom:3px solid var(--blue-dark);background:var(--white)}
.brand{position:absolute;left:59px;top:14px;display:flex;align-items:center;gap:8px}
.brand-dot{width:34px;height:34px;border-radius:50%;background:var(--blue-dark)}
.brand-name{font-size:17px;font-weight:800;color:var(--blue-dark);line-height:1}
.brand-tag{font-size:9px;font-weight:800;color:var(--blue-dark);letter-spacing:1px;margin-top:3px}
.main-nav{position:absolute;left:370px;top:27px;display:flex;font-size:13px;font-weight:500}
.main-nav a{margin-right:58px}
.main-nav a.active{color:var(--blue-dark)}
.header-tools{position:absolute;right:0;top:0;width:215px;height:68px;background:var(--blue-pale);clip-path:polygon(18px 0,100% 0,100% 100%,0 100%)}
.tool{position:absolute;top:21px;width:28px;height:28px;border-radius:50%;background:var(--white);display:flex;align-items:center;justify-content:center}

/* hero */
.hero-card{position:absolute;top:90px;height:286px;overflow:hidden}
.hero-1{left:57px;width:320px;background:var(--blue-pale)}
.hero-2{left:391px;width:419px;background:linear-gradient(120deg,var(--blue-dark) 40%,var(--blue) 75%,#7fb6e0)}
.hero-3{left:825px;width:319px;background:var(--blue-pale)}
.btn{display:inline-block;border-radius:14px;font-size:12.5px;font-weight:600;padding:6px 17px}
.btn-blue{background:var(--blue-dark);color:var(--white)}
.btn-white{background:var(--white);color:var(--blue-dark)}
.photo{position:absolute}

/* about */
.about-title{left:562px;top:424px;font-size:28px;font-weight:800}
.about-sub{left:562px;top:460px;font-size:19px;color:var(--blue-dark)}
.about-text{left:562px;top:493px;width:565px;font-size:13px;line-height:21px;color:var(--text)}

/* popular */
.section-title{left:0;width:1200px;text-align:center;font-size:28px;font-weight:800}
.rule{width:42px;height:2px;background:var(--blue-dark);left:579px}
.tabs{top:910px;left:0;width:1200px;display:flex;justify-content:center;gap:70px;font-size:16px;color:#444}
.tabs .on{color:var(--blue-dark)}
.shop-panel{left:56px;top:962px;width:1088px;height:596px;background:var(--blue-pale)}
.filter{left:70px;top:976px;width:253px;height:542px;background:var(--white)}
.search{position:absolute;left:29px;top:21px;width:190px;height:22px;border:1px solid var(--blue-dark);border-radius:12px;font-size:11px;padding:4px 11px;color:#444}
.cat-list{position:absolute;left:29px;top:59px;font-size:12.5px;color:#333;list-style:none}
.cat-list li{margin-bottom:14px}
.cat-list li.open{color:var(--blue-dark);margin-bottom:4px}
.cat-list .sub{font-size:11px;color:#444;margin:0 0 14px 9px;line-height:14px}
.product{position:absolute;width:240px;height:240px;background:var(--white)}
.product .pic{position:absolute;left:70px;top:12px;width:100px;height:100px;border-radius:4px}
.product h3{position:absolute;left:27px;top:132px;width:190px;font-size:14px;font-weight:500;color:var(--blue-dark);line-height:17px}
.product p{position:absolute;left:27px;top:176px;width:180px;font-size:10.5px;line-height:14px;color:#222}
.product .price{position:absolute;left:27px;top:208px;font-size:14px;color:var(--blue-dark)}
.product .cart{position:absolute;right:34px;top:206px}
.pager{position:absolute;top:1482px;width:26px;height:26px;background:var(--blue-dark);display:flex;align-items:center;justify-content:center}

/* categories */
.tile{position:absolute;top:1610px;height:294px;overflow:hidden}
.tile .label{position:absolute;left:0;bottom:0;width:100%;height:62px;display:flex;align-items:center;justify-content:center;color:var(--white);font-size:19px;font-weight:500}

/* testimonial */
.quote-box{left:193px;top:2125px;width:507px;height:232px;background:#f3f3f3;border-right:3px solid var(--blue-dark);text-align:center}
.quote-box h4{margin-top:27px;font-size:19px;font-weight:600;color:var(--blue-dark)}
.quote-box .role{font-size:12.5px;margin-top:5px}
.quote-box .quote{margin:22px 36px 0;font-size:13px;line-height:21px;color:#555}
.qm{color:var(--blue-dark);font-weight:800;font-size:18px}
.stars{margin-top:4px;color:var(--blue-dark);font-size:13px;letter-spacing:1px}
.stars span{color:#ccc}
.slide-btn{position:absolute;z-index:2;width:17px;height:17px;background:var(--blue-dark);display:flex;align-items:center;justify-content:center}

/* footer */
.footer-main{left:0;top:2405px;width:1200px;height:184px;background:var(--blue-dark);color:var(--white)}
.footer-bar{left:0;top:2589px;width:1200px;height:45px;background:var(--blue);color:var(--white)}
.news-title{left:221px;top:2433px;font-size:16px;font-weight:500}
.news-form{left:220px;top:2466px;width:279px;height:26px;border:1px solid var(--white);border-radius:14px;font-size:12px;padding:6px 14px}
.news-send{position:absolute;right:3px;top:2px;width:70px;height:20px;border-radius:10px;background:var(--white);color:var(--blue-dark);font-size:12px;text-align:center;line-height:20px}
.divider{left:599px;top:2448px;height:110px;border-left:1px dashed rgba(255,255,255,.6)}
.f-line{display:flex;align-items:flex-start;gap:10px;font-size:15.5px;line-height:18px}
.pay{position:absolute;top:2603px;width:32px;height:20px;border:1.5px solid var(--white);border-radius:3px}
.social{position:absolute;top:2601px;width:22px;height:22px;border:1.5px solid var(--white);border-radius:3px}
.legal{position:absolute;top:2606px;font-size:13px;font-weight:500}
</style>
</head>
<body>

<header class="site-header">
  <div class="brand">
    <div class="brand-dot"></div>
    <div>
      <div class="brand-name">QUILL PET</div>
      <div class="brand-tag">PREMIUM PET FOOD</div>
    </div>
  </div>
  <nav class="main-nav">
    <a class="active" href="#">ABOUT US</a>
    <a href="#">HOLDER</a>
    <a href="#">DOG</a>
    <a href="#">CAT</a>
    <a href="#">CONTACT</a>
  </nav>
  <div class="header-tools">
    <div class="tool" style="left:62px">
      <svg width="14" height="14" viewBox="0 0 24 24" fill="none" stroke="#0054AA" stroke-width="2"><path d="M2 3h3l3 12h11l2-8H7"/><circle cx="9" cy="20" r="1.5"/><circle cx="18" cy="20" r="1.5"/></svg>
    </div>
    <div class="abs" style="left:83px;top:21px;width:7px;height:7px;border-radius:50%;background:var(--blue-dark)"></div>
    <div class="tool" style="left:96px">
      <svg width="14" height="14" viewBox="0 0 24 24" fill="none" stroke="#0054AA" stroke-width="2.2"><circle cx="10" cy="10" r="7"/><path d="M15 15l6 6"/></svg>
    </div>
    <div class="tool" style="left:130px">
      <svg width="14" height="14" viewBox="0 0 24 24" fill="none" stroke="#0054AA" stroke-width="2"><circle cx="12" cy="8" r="4"/><path d="M4 21c0-4 4-6 8-6s8 2 8 6"/></svg>
    </div>
  </div>
</header>

<!-- hero -->
<section class="hero-card hero-1">
  <div class="abs" style="left:15px;top:20px;font-size:40px;font-weight:800;color:var(--blue-dark);line-height:44px">Tasty Food</div>
  <div class="abs" style="left:15px;top:68px;font-size:36px;font-weight:400;color:var(--blue-dark)">For Cats</div>
  <div class="abs" style="left:15px;top:117px;font-size:13px">organic and fresh</div>
  <a class="btn btn-blue abs" style="left:17px;top:143px" href="#">Shop Now</a>
  <div class="photo" role="img" aria-label="Bowl of dry cat food" style="left:202px;top:58px;width:96px;height:96px;border-radius:50%;background:radial-gradient(circle,#8a5a2e,#5b3a1e 65%,#2f5c70 70%)"></div>
  <div class="photo" role="img" aria-label="Cat food package" style="left:70px;top:182px;width:48px;height:82px;background:linear-gradient(#f6f6f6,#e8d8d0)"></div>
  <div class="photo" role="img" aria-label="White cat lying" style="left:190px;top:180px;width:130px;height:106px;background:linear-gradient(160deg,#f5f5f5,#dcdcdc);border-radius:40px 40px 0 0"></div>
</section>

<section class="hero-card hero-2">
  <div class="abs" style="left:23px;top:17px;font-size:38px;font-weight:400;color:var(--white)">We Provide</div>
  <div class="abs" style="left:23px;top:61px;font-size:40px;font-weight:800;color:var(--white)">Best Food</div>
  <div class="abs" style="left:23px;top:116px;width:215px;font-size:12.5px;line-height:15px;color:var(--white)">delicious food enhances health and love</div>
  <a class="btn btn-white abs" style="left:23px;top:158px" href="#">Shop Now</a>
  <div class="photo" role="img" aria-label="Beagle dog sitting" style="left:258px;top:30px;width:150px;height:256px;background:linear-gradient(#c88a4a,#e8d6c0 60%,#f0e8dc);border-radius:70px 70px 0 0;opacity:.9"></div>
  <div class="photo" role="img" aria-label="Bowl of dog food with treats" style="left:130px;top:176px;width:130px;height:74px;border-radius:50%;background:radial-gradient(ellipse,#d8b24a,#c0c4c8 60%)"></div>
</section>

<section class="hero-card hero-3">
  <div class="abs" style="left:0;top:10px;width:319px;text-align:center;font-size:36px;font-weight:600;color:var(--blue-dark)">Quality Pet Food</div>
  <div class="abs" style="left:40px;top:59px;width:239px;text-align:center;font-size:12.5px;line-height:15px;color:#444">Dogs, Cats, Rabbits, Birds, Rodents, Snakes And Fish</div>
  <a class="btn btn-blue abs" style="left:112px;top:98px" href="#">Order Now</a>
  <div class="photo" role="img" aria-label="Dog, cat and rabbit together with a chick and butterfly" style="left:0;top:150px;width:319px;height:136px;background:linear-gradient(90deg,#2a2a2a,#7a7a7a 45%,#5a5a5a 70%,#222)"></div>
</section>

<!-- about -->
<svg class="abs" style="left:0;top:372px" width="1200" height="475" viewBox="0 0 1200 475" aria-hidden="true">
  <defs><linearGradient id="aboutBg" x1="0" x2="1"><stop offset="0" stop-color="#E8F1F8"/><stop offset="1" stop-color="#ffffff"/></linearGradient></defs>
  <path d="M0 5 C120 40 220 50 420 32 C700 8 900 40 1200 0 L1200 215 C1000 340 820 450 500 430 C300 418 150 452 0 475 Z" fill="url(#aboutBg)"/>
</svg>
<div class="photo" role="img" aria-label="Dog with sunglasses, cat, rooster and mouse in a party hat" style="left:70px;top:505px;width:400px;height:250px;background:radial-gradient(ellipse at 40% 60%,#7d7d7d,#b8b8b8 55%,rgba(232,241,248,0) 75%)"></div>
<h2 class="abs about-title">ABOUT QUILL PET</h2>
<div class="abs about-sub">Premium Pet Food</div>
<p class="abs about-text">It is a long established fact that a reader will be distracted by the readable content of a page when looking at its layout. The point of using Lorem Ipsum is that it has a more-or-less normal distribution of letters, as opposed to using 'Content here, content here', making it look like readable English. Many desktop publishing packages and web page editors now use Lorem Ipsum as their default model text, and a search for 'lorem ipsum' will uncover many web sites still in their infancy.</p>
<a class="btn btn-blue abs" style="left:563px;top:638px" href="#">Read More</a>

<!-- popular items -->
<h2 class="abs section-title" style="top:843px">POPULAR ITEMS</h2>
<div class="abs rule" style="top:892px"></div>
<div class="abs tabs"><span class="on">Dog</span><span>Cat</span><span>Rodents</span><span>Bird</span></div>

<div class="abs shop-panel"></div>
<aside class="abs filter">
  <div class="search">Search
    <svg style="position:absolute;right:8px;top:5px" width="11" height="11" viewBox="0 0 24 24" fill="none" stroke="#0054AA" stroke-width="2.4"><circle cx="10" cy="10" r="7"/><path d="M15 15l6 6"/></svg>
  </div>
  <ul class="cat-list">
    <li class="open">BARF &nbsp;⌵</li>
    <li class="sub">Ergänzungsfuttermittel Für Hunde<br>&amp; Katzen Bio</li>
    <li>HUND &nbsp;⌵</li>
    <li>KAUARTIKEL &nbsp;⌵</li>
    <li>FRAUCHEN UND HERRCHEN &nbsp;⌵</li>
    <li>KATZE &nbsp;⌵</li>
    <li>SCHILDKRÖTEN &nbsp;⌵</li>
    <li>NAGER &nbsp;⌵</li>
    <li>TERRARISTIK &nbsp;⌵</li>
    <li>TIERGESUNDHEIT &nbsp;⌵</li>
    <li>WILDTIERE &nbsp;⌵</li>
  </ul>
</aside>

<article class="product" style="left:342px;top:976px">
  <div class="pic" role="img" aria-label="Oil bottles with fish" style="background:linear-gradient(#3a2e1a,#6b5a30 60%,#c0c4c8)"></div>
  <h3>NVK Vital Omega 3-6-9 Öl 250ml</h3>
  <p>It Is A Long Established Fact That A Reader Will Be ⟶</p>
  <div class="price">CHF 19.90</div>
  <svg class="cart" width="18" height="17" viewBox="0 0 24 22" fill="none" stroke="#0054AA" stroke-width="2"><path d="M1 2h4l3 12h12l2-8H7"/><circle cx="9" cy="19" r="1.5"/><circle cx="18" cy="19" r="1.5"/></svg>
</article>
<article class="product" style="left:596px;top:976px">
  <div class="pic" role="img" aria-label="Supplement tub" style="background:linear-gradient(#f4f4f4,#e0e0e0 60%,#8cc46a)"></div>
  <h3>NVK Darm Plus 150g</h3>
  <p>It Is A Long Established Fact That A Reader Will Be ⟶</p>
  <div class="price">CHF 49.00</div>
  <svg class="cart" width="18" height="17" viewBox="0 0 24 22" fill="none" stroke="#0054AA" stroke-width="2"><path d="M1 2h4l3 12h12l2-8H7"/><circle cx="9" cy="19" r="1.5"/><circle cx="18" cy="19" r="1.5"/></svg>
</article>
<article class="product" style="left:849px;top:976px">
  <div class="pic" role="img" aria-label="Kraft paper supplement bag" style="left:80px;width:80px;background:linear-gradient(#c8a888,#a88868)"></div>
  <h3>NVK Seealgen Pulver 500g</h3>
  <p>It Is A Long Established Fact That A Reader Will Be ⟶</p>
  <div class="price">CHF 11.90</div>
  <svg class="cart" width="18" height="17" viewBox="0 0 24 22" fill="none" stroke="#0054AA" stroke-width="2"><path d="M1 2h4l3 12h12l2-8H7"/><circle cx="9" cy="19" r="1.5"/><circle cx="18" cy="19" r="1.5"/></svg>
</article>
<article class="product" style="left:342px;top:1230px">
  <div class="pic" role="img" aria-label="Orange supplement bag" style="left:85px;width:70px;background:linear-gradient(#e06020,#b03a10)"></div>
  <h3>NVK Muschelextrakt 100g</h3>
  <p>It Is A Long Established Fact That A Reader Will Be ⟶</p>
  <div class="price">CHF 17.20</div>
  <svg class="cart" width="18" height="17" viewBox="0 0 24 22" fill="none" stroke="#0054AA" stroke-width="2"><path d="M1 2h4l3 12h12l2-8H7"/><circle cx="9" cy="19" r="1.5"/><circle cx="18" cy="19" r="1.5"/></svg>
</article>
<article class="product" style="left:596px;top:1230px">
  <div class="pic" role="img" aria-label="Cod liver oil bottle with fish" style="background:linear-gradient(90deg,#9a8a70,#2a2418 45%,#2a2418 55%,#9a8a70)"></div>
  <h3>NVK Dorschlebertran 250ml</h3>
  <p>It Is A Long Established Fact That A Reader Will Be ⟶</p>
  <div class="price">CHF 13.70</div>
  <svg class="cart" width="18" height="17" viewBox="0 0 24 22" fill="none" stroke="#0054AA" stroke-width="2"><path d="M1 2h4l3 12h12l2-8H7"/><circle cx="9" cy="19" r="1.5"/><circle cx="18" cy="19" r="1.5"/></svg>
</article>
<article class="product" style="left:849px;top:1230px">
  <div class="pic" role="img" aria-label="Minced chicken meat" style="left:68px;top:36px;width:104px;height:70px;background:linear-gradient(#4a5a48,#c05060 55%,#d8c8b8)"></div>
  <h3>Grand Pet Pouletfleisch Gehackt 2 X 250g</h3>
  <p>It Is A Long Established Fact That A Reader Will Be ⟶</p>
  <div class="price">CHF 4.00</div>
  <svg class="cart" width="18" height="17" viewBox="0 0 24 22" fill="none" stroke="#0054AA" stroke-width="2"><path d="M1 2h4l3 12h12l2-8H7"/><circle cx="9" cy="19" r="1.5"/><circle cx="18" cy="19" r="1.5"/></svg>
</article>
<div class="pager" style="left:1033px"><svg width="14" height="12" viewBox="0 0 14 12" fill="none" stroke="#fff" stroke-width="1.6"><path d="M13 6H1M6 1L1 6l5 5"/></svg></div>
<div class="pager" style="left:1063px"><svg width="14" height="12" viewBox="0 0 14 12" fill="none" stroke="#fff" stroke-width="1.6"><path d="M1 6h12M8 1l5 5-5 5"/></svg></div>

<!-- categories -->
<a class="tile" href="#" style="left:2px;width:295px">
  <div class="photo" role="img" aria-label="Happy beagle with dog food" style="inset:0;background:linear-gradient(#dcdcde,#c8b8a0 70%,#8a5a2a)"></div>
  <div class="label" style="background:rgba(20,20,20,.82)">DOG FOOD</div>
</a>
<a class="tile" href="#" style="left:302px;width:295px">
  <div class="photo" role="img" aria-label="Curly cat eating from a bowl" style="inset:0;background:linear-gradient(#e4b4b8,#a89a88 60%,#7a6a58)"></div>
  <div class="label" style="background:rgba(6,119,186,.88)">CAT FOOD</div>
</a>
<a class="tile" href="#" style="left:602px;width:295px">
  <div class="photo" role="img" aria-label="Hamster eating from a plate" style="inset:0;background:linear-gradient(#c8a878,#e8e4de 50%,#8a8078)"></div>
  <div class="label" style="background:rgba(6,119,186,.85)">RODENTS FOOD</div>
</a>
<a class="tile" href="#" style="left:902px;width:296px">
  <div class="photo" role="img" aria-label="Oriole bird on an orange" style="inset:0;background:linear-gradient(100deg,#5a7048,#8a9a68 50%,#e8a030)"></div>
  <div class="label" style="background:rgba(123,173,215,.85)">BIRD FOOD</div>
</a>

<!-- testimonials -->
<h2 class="abs section-title" style="top:1956px">WHAT OUR CLIENTS SAY</h2>
<div class="abs rule" style="top:2004px"></div>
<div class="photo" role="img" aria-label="Client portrait on the phone" style="left:678px;top:2068px;width:328px;height:257px;background:linear-gradient(var(--blue-pale),#d8d4d0 50%,#a08a70)"></div>
<div class="abs quote-box">
  <h4>Lena M. Hart</h4>
  <div class="role">Php Developer</div>
  <p class="quote"><span class="qm">“</span> It is a long established fact that a reader will be distracted by the readable content of a page when looking at its layout. The point of using Lorem Ipsum is that it has a more-or-less normal distribution of letters, as opposed to using 'Content here, content here', making it look like readable English. <span class="qm">”</span></p>
  <div class="stars">★★★★<span>★</span></div>
</div>
<div class="slide-btn" style="left:210px;top:2110px"><svg width="8" height="10" viewBox="0 0 8 10" fill="none" stroke="#fff" stroke-width="1.5"><path d="M2 1l4 4-4 4"/></svg></div>
<div class="slide-btn" style="left:193px;top:2127px"><svg width="8" height="10" viewBox="0 0 8 10" fill="none" stroke="#fff" stroke-width="1.5"><path d="M6 1L2 5l4 4"/></svg></div>

<!-- footer -->
<footer>
  <div class="abs footer-main"></div>
  <div class="abs news-title" style="color:#fff">Subscribe to our newsletter</div>
  <div class="abs news-form" style="color:#fff">your email<span class="news-send">SEND</span></div>
  <div class="abs f-line" style="left:221px;top:2521px;color:#fff">
    <svg width="20" height="24" viewBox="0 0 20 24" fill="none" stroke="#fff" stroke-width="1.6"><path d="M10 23s8-8 8-13a8 8 0 0 0-16 0c0 5 8 13 8 13z"/><circle cx="10" cy="10" r="3"/></svg>
    <span style="margin-left:6px">QUILL-PET GmbH, Lindenweg 42,<br>8000 Zürich</span>
  </div>
  <div class="abs divider"></div>
  <div class="abs f-line" style="left:693px;top:2445px;color:#fff">
    <svg width="18" height="18" viewBox="0 0 24 24" fill="none" stroke="#fff" stroke-width="1.6"><path d="M5 2h4l2 5-3 2a12 12 0 0 0 7 7l2-3 5 2v4a2 2 0 0 1-2 2A19 19 0 0 1 3 4a2 2 0 0 1 2-2z"/></svg>
    <span>044 555 01 23</span>
  </div>
  <div class="abs f-line" style="left:694px;top:2482px;color:#fff">
    <svg width="17" height="14" viewBox="0 0 24 18" fill="none" stroke="#fff" stroke-width="1.6"><rect x="1" y="1" width="22" height="16"/><path d="M1 1l11 9 11-9"/></svg>
    <span>info@quill-pet.ch</span>
  </div>
  <div class="abs f-line" style="left:693px;top:2512px;color:#fff">
    <svg width="18" height="18" viewBox="0 0 24 24" fill="none" stroke="#fff" stroke-width="1.6" style="margin-top:8px"><circle cx="12" cy="12" r="10"/><path d="M12 6v6l4 2"/></svg>
    <span>Mo - Fr 08:30 - 12:00 / 13:00 - 18:00<br>Sa 09:00 - 16:00</span>
  </div>

  <div class="abs footer-bar"></div>
  <div class="pay" style="left:100px"></div>
  <div class="pay" style="left:141px"></div>
  <div class="pay" style="left:182px"></div>
  <div class="pay" style="left:223px"></div>
  <a class="legal" href="#" style="left:504px;color:#fff">TERMS OF USE</a>
  <a class="legal" href="#" style="left:628px;color:#fff">IMPRINT</a>
  <div class="social" style="left:1092px"></div>
  <div class="social" style="left:1121px"></div>
</footer>

</body>
</html>
```